Storefront signage for Physio clinic

We need a design for our storefront windows at our physiotherapy & Pilates clinic.

The design should be modern and include our logo, website url and services (physiotherapy, pilates, massage).

Some inspirational exercise/pilates/recovery quotes may be included and I would like to see the use of sport/pilates/injury related stock images. I have attached a few examples of what we want (images numbered 1-5). And I have attached our current design and photo of the outside of our clinic.

In the attached images there is also a pdf with measurments of our window panels. We require signage for the areas marked 1-10. As you can see on our current signage, you don't need to have a separate image for each panel, these can flow onto each other.

Industry/Entity Type

Clinic

Colors
85acd3
3377b5
3277b5
e8e8e8
c3c3c3
9d9d9d
848484
7f7f7f

Requirements
Must have
• Stock images related to sports, physiotherapy and pilates
• Ideally these images should be in greyscale and blend in with the rest of the panel which should include colours.
• I would like to see for example a runner, a weightlifter, someone doing pilates, someone with back pain (not necessarily all of these).
Should not have
• I want a creative, modern, up market design, not just a standard recycled template.

```html
<!DOCTYPE html>
<html lang="en">
<head>
<meta charset="utf-8">
<title>Harbourline Physiotherapy &amp; Pilates – Window Signage</title>
<link rel="stylesheet" href="https://fonts.googleapis.com/css2?family=Oswald:wght@400;500;600&display=swap">
<style>
  :root {
    --navy: #1f3f86;
    --blue: #3377b5;
    --sky: #85acd3;
    --mid-blue: #5a88c9;
    --light: #e8e8e8;
    --silver: #c3c3c3;
    --grey: #848484;
    --massage-grey: #7f7f7f;
    --white: #ffffff;
    --stage: #eef0f3;
  }
  * { margin: 0; padding: 0; box-sizing: border-box; }
  html, body { width: 1200px; height: 715px; overflow: hidden; }
  body {
    background: var(--stage);
    font-family: "Oswald", "Arial Narrow", sans-serif;
    position: relative;
  }

  /* Brand lockup */
  .brand { display: flex; align-items: center; gap: 10px; color: var(--blue); font-weight: 500; }
  .brand-dot { border-radius: 50%; background: var(--blue); flex: none; }
  .brand-name { line-height: 1; letter-spacing: 0.5px; }
  .brand-tag { line-height: 1.2; }

  /* Landscape services panel */
  .services-panel {
    position: absolute; left: 40px; top: 125px; width: 740px; height: 465px;
    background: linear-gradient(180deg, #f6f8fc 0%, #dde5f1 100%);
    overflow: hidden;
  }
  .services-photo {
    position: absolute; left: 0; top: 0; width: 300px; height: 100%;
    background: linear-gradient(160deg, #c9d2e2 0%, #8e9bb3 45%, #b6c2d6 100%);
  }
  .services-panel .brand { position: absolute; left: 420px; top: 40px; }
  .services-panel .brand-dot { width: 44px; height: 44px; }
  .services-panel .brand-name { font-size: 28px; }
  .services-panel .brand-tag { font-size: 11px; }
  .services-shapes { position: absolute; left: 300px; top: 0; width: 440px; height: 465px; }
  .service-label { fill: var(--white); font-family: "Oswald", sans-serif; font-size: 18px; text-anchor: middle; }
  .call-bar {
    position: absolute; right: 0; bottom: 22px; width: 400px; height: 58px;
    background: var(--blue); color: var(--white);
    display: flex; align-items: center; gap: 14px; padding-left: 34px;
    clip-path: polygon(6% 0, 100% 0, 100% 100%, 0 100%);
  }
  .call-bar .call-label { font-size: 17px; font-weight: 500; }
  .call-bar .call-number { font-size: 34px; font-weight: 500; letter-spacing: 0.5px; }

  /* Portrait motto panel */
  .motto-panel {
    position: absolute; left: 820px; top: 45px; width: 340px; height: 625px;
    background: var(--white); overflow: hidden;
  }
  .motto-header { height: 135px; display: flex; align-items: center; justify-content: center; }
  .motto-panel .brand-dot { width: 48px; height: 48px; }
  .motto-panel .brand-name { font-size: 30px; }
  .motto-panel .brand-tag { font-size: 12px; }
  .motto-photo {
    position: absolute; left: 0; top: 135px; width: 100%; height: 490px;
    background: linear-gradient(170deg, #c6cfe0 0%, #8895ae 50%, #3b4a6a 100%);
  }
  .motto-swoosh { position: absolute; left: 0; top: 135px; width: 340px; height: 490px; }
  .motto-text {
    position: absolute; left: 26px; bottom: 40px; width: 280px;
    color: var(--white); font-weight: 600; line-height: 0.95;
    border-left: 3px solid var(--navy); border-bottom: 3px solid var(--navy);
    padding: 6px 0 6px 10px;
  }
  .motto-text .line-one { font-size: 50px; display: block; }
  .motto-text .line-two { font-size: 42px; display: block; }
</style>
</head>
<body>

  <section class="services-panel">
    <div class="services-photo" role="img" aria-label="Greyscale photo of an athlete from behind holding her lower back, with a red glow marking the pain"></div>

    <svg class="services-shapes" viewBox="0 0 440 465" aria-hidden="true">
      <path d="M250 300 C330 220 380 210 440 200 L440 465 L230 465 Z" fill="#ffffff" opacity="0.7"/>
      <circle cx="125" cy="315" r="65" fill="var(--massage-grey)"/>
      <circle cx="230" cy="320" r="62" fill="var(--mid-blue)"/>
      <circle cx="185" cy="210" r="74" fill="var(--navy)"/>
      <text class="service-label" x="185" y="216">PHYSIOTHERAPY</text>
      <text class="service-label" x="112" y="322">MASSAGE</text>
      <text class="service-label" x="240" y="326">PILATES</text>
    </svg>

    <div class="brand">
      <span class="brand-dot"></span>
      <div>
        <div class="brand-name">HARBOURLINE</div>
        <div class="brand-tag">Physiotherapy &amp; Pilates</div>
      </div>
    </div>

    <div class="call-bar">
      <span class="call-label">CALL US NOW:</span>
      <span class="call-number">555-010-482</span>
    </div>
  </section>

  <section class="motto-panel">
    <header class="motto-header">
      <div class="brand">
        <span class="brand-dot"></span>
        <div>
          <div class="brand-name">HARBOURLINE</div>
          <div class="brand-tag">Physiotherapy &amp; Pilates</div>
        </div>
      </div>
    </header>

    <div class="motto-photo" role="img" aria-label="Greyscale photo of a woman seen from behind holding her neck, with a red glow marking the pain"></div>

    <svg class="motto-swoosh" viewBox="0 0 340 490" aria-hidden="true">
      <path d="M300 200 C250 280 250 380 290 490 L340 490 L340 190 Z" fill="var(--blue)"/>
      <path d="M200 490 C230 420 270 380 340 330 L340 490 Z" fill="var(--mid-blue)"/>
      <path d="M330 120 C300 160 300 200 320 230 L340 230 L340 120 Z" fill="var(--blue)" opacity="0.85"/>
    </svg>

    <p class="motto-text">
      <span class="line-one">IF YOU REST</span>
      <span class="line-two">YOU RUST</span>
    </p>
  </section>

</body>
</html>
```